Package Design for 15 lines of Tea

I need design variations for 15 different Tea lines.
The tea will be packaged in Tin cylinders.
I have attached several pictures to show you an example of the display we are modelling after along with other references.
The 15 tea lines are:
Study Tea
Ingredients: Brazilian Mate, Mint
Energy Boost Tea
Ingredients: Yunnan Coffee, Dark Puer
Relaxation Tea
Ingredients: Lotus Flower, South African Rooibos
Beauty Tea
Ingredients: Rose, Chrysanthemum, Red Dates, Huangqi
Sore Throat Tea
Ingredients: Honeysuckle, Pang Da Hai, Chamomile, Licorice Root
Get Well Tea
Ingredients: Ginger, Rooibos, Orange peel, Chinese Angelica
Diet Tea
Ingredients: Puer, Hibiscus, Lemongrass, Lotus Plumule
Bedtime Tea
Ingredients: Apple, Orange, Chamomile
South African Rooibos Tea
(pure)
Brazilian Yerba Mate Tea
(pure)
Long Jing Green Tea
(pure)
Darjeeling Black Tea
(pure)
Nepal Golden Tea
(Pure)
Bai Mu Dan White Tea
(pure)
Phoenix Oolong Tea
(pure)
Every Tea Blend should have three unique symbols that describe the purpose and theme of the blend. (!!Please don't make specific reference to the ingredients of the blends because some of these ingredients may be changed later. Stick to focusing on the intended purpose of the tea blend!!)
I would like the symbols to keep the same brushlike style that is consistent with our company logo.
Please keep the three block structure. I suggest keeping to just one color per tea blend. This will help each blend stand out between one another. I have a sample of the "Diet Tea" attached that I did myself to give you an idea of the structure I'm looking for, but obviously it's just my amateur version. Hope you can make them look far more appealing.
The ultimate goal is to build a picture language unique to our brand. As more products are released, we intend to potentially have hundreds of symbols, each with it's own meaning. So it would be nice when you present your pictures if you explain its intended meaning or message.
Deminsions:
Cylinder type 1: 82mm*38mmH
circular labels (along with your design) will be placed on the cap of product, and then the cylinder will be slanted on it's side to display the cap towards the customer.
Cylinder type 2: 65mm*152mmH
the labels will be placed on the side of the cylinder. In this version, try lining the three symbols in a vertical position. If this looks awful to you then feel free to go back to the horizontal style, but it would be nice to see what the vertical version looks like for reference.
Updates
Due to the scope of this project, please take note that I just increased my budget an additional 500 dollars more.
I also just added a 100 dollar second place prize. Don't want to see hard work unrewarded.
Feel free to send a few samples and I will provide prompt feedback. Please don't feel that you must submit all 15 lines at the same time.
Project Deadline Extended
Reason: I am extending the deadline as I feel there are more detailed revisions that need to be made until final selection.
Target Market(s)
Middle to Upper Class Consumers in China
Industry/Entity Type
It Company
Other font styles liked:
- font similar to font on company logo
Requirements
Must have
- Tea Designs must be in harmony with company logo and theme.
Should not have
- Avoid using Chinese characters as symbols. They may seem cool to westerners, but it's tacky for Chinese consumers.

```html
<!DOCTYPE html>
<html lang="en">
<head>
<meta charset="utf-8">
<title>Lumen Leaf – Cap Labels</title>
<link href="https://fonts.googleapis.com/css2?family=Alegreya:wght@800&family=Open+Sans:wght@400;600&display=swap" rel="stylesheet">
<style>
  :root {
    --bg-top: #f2f2f2;
    --bg-bottom: #d4d4d4;
    --ink-dark: #1a1a1a;
    --white: #ffffff;
    --beauty-a: #8a4aa6;
    --beauty-b: #5e2a7e;
    --energy-a: #e6a321;
    --energy-b: #b8502b;
    --study-a: #4aa3d0;
    --study-b: #1f5f92;
  }
  * { box-sizing: border-box; margin: 0; padding: 0; }
  html, body { width: 1200px; height: 962px; overflow: hidden; }
  body {
    background: linear-gradient(180deg, var(--bg-top), var(--bg-bottom));
    position: relative;
    font-family: "Open Sans", sans-serif;
  }
  .brand-name {
    position: absolute;
    top: 44px;
    right: 52px;
    font-family: "Open Sans", sans-serif;
    font-weight: 600;
    font-size: 26px;
    color: var(--ink-dark);
  }
  .cap-label {
    position: absolute;
    width: 320px;
    height: 320px;
    border-radius: 50%;
    color: var(--white);
    box-shadow: 0 10px 24px rgba(0,0,0,0.18);
  }
  .cap-label--beauty { left: 90px;  top: 300px; background: linear-gradient(150deg, var(--beauty-a), var(--beauty-b)); }
  .cap-label--energy { left: 440px; top: 300px; background: linear-gradient(30deg, var(--energy-b), var(--energy-a)); }
  .cap-label--study  { left: 790px; top: 300px; background: linear-gradient(30deg, var(--study-b), var(--study-a)); }
  .cap-label__ring {
    position: absolute;
    inset: 14px;
    border: 3px solid rgba(255,255,255,0.85);
    border-radius: 50%;
  }
  .cap-label__title {
    position: absolute;
    top: 72px;
    width: 100%;
    text-align: center;
    font-family: "Alegreya", serif;
    font-weight: 800;
    font-size: 38px;
  }
  .cap-label__purpose {
    position: absolute;
    top: 130px;
    left: 52px;
    right: 30px;
    display: flex;
    align-items: flex-start;
    gap: 12px;
  }
  .cap-label__symbols {
    flex: 0 0 72px;
    height: 22px;
    border-radius: 3px;
    background: rgba(255,255,255,0.25);
  }
  .cap-label__ingredients {
    font-size: 11px;
    line-height: 1.3;
    white-space: nowrap;
  }
  .cap-label__brand {
    position: absolute;
    top: 200px;
    width: 100%;
    text-align: center;
    font-size: 17px;
  }
</style>
</head>
<body>
  <div class="brand-name">Lumen Leaf</div>

  <div class="cap-label cap-label--beauty">
    <div class="cap-label__ring"></div>
    <div class="cap-label__title">Beauty Tea</div>
    <div class="cap-label__purpose">
      <div class="cap-label__symbols" role="img" aria-label="Three brush-style symbols for beauty: sparkle, heart, shine"></div>
      <div class="cap-label__ingredients">Rose, Chrysanthemum,<br>Red Dates &amp; Huangqi</div>
    </div>
    <div class="cap-label__brand">Lumen Leaf</div>
  </div>

  <div class="cap-label cap-label--energy">
    <div class="cap-label__ring"></div>
    <div class="cap-label__title">Energy Tea</div>
    <div class="cap-label__purpose">
      <div class="cap-label__symbols" role="img" aria-label="Three brush-style symbols for energy: lightning, renewal, rising chart"></div>
      <div class="cap-label__ingredients">Yunnan Coffee<br>&amp; Dark Puer</div>
    </div>
    <div class="cap-label__brand">Lumen Leaf</div>
  </div>

  <div class="cap-label cap-label--study">
    <div class="cap-label__ring"></div>
    <div class="cap-label__title">Study Tea</div>
    <div class="cap-label__purpose">
      <div class="cap-label__symbols" role="img" aria-label="Three brush-style symbols for study: pencil, open book, laptop"></div>
      <div class="cap-label__ingredients">Brazilian Mate<br>&amp; Mint</div>
    </div>
    <div class="cap-label__brand">Lumen Leaf</div>
  </div>
</body>
</html>
```